Business cards design on a high standard

We advise clients on insurance and financial matters, since these clients pay for our advice, the design should have a high standard. Our logo should be included. From the colors we are open for everything.

Colors

Designer to choose colors to be used in the design.

```html
<!DOCTYPE html>
<html lang="en">
<head>
<meta charset="utf-8">
<title>Alpine Counsel — Business Cards</title>
<link href="https://fonts.googleapis.com/css2?family=Lato:wght@400;700&display=swap" rel="stylesheet">
<style>
  :root {
    --backdrop: #2a2a2a;
    --brand-red: #dc0201;
    --paper: #ffffff;
    --ink: #1e1e1e;
    --rule: #a8a8a8;
  }
  * { margin: 0; padding: 0; box-sizing: border-box; }
  html, body {
    width: 1200px; height: 1200px; overflow: hidden;
    background: var(--backdrop);
    font-family: "Lato", Arial, sans-serif;
  }
  .canvas { position: relative; width: 1200px; height: 1200px; }
  .card {
    position: absolute; top: 310px; height: 594px;
    box-shadow: 0 4px 10px rgba(0,0,0,0.45);
  }
  .card--front { left: 234px; width: 364px; background: var(--paper); }
  .card--back { left: 627px; width: 369px; background: var(--brand-red); }

  .wordmark {
    position: absolute; left: 0; right: 0; text-align: center;
    font-family: "Lato", Arial, sans-serif; font-weight: 700; line-height: 1;
  }
  .wordmark__main { display: block; font-size: 50px; letter-spacing: 2px; }
  .wordmark__sub { display: block; font-size: 21px; letter-spacing: 6px; margin-top: 6px; }
  .card--front .wordmark { top: 150px; color: var(--brand-red); }
  .card--back .wordmark { top: 278px; color: var(--paper); }
  .card--back .wordmark__main { font-size: 54px; }
  .card--back .wordmark__sub { font-size: 23px; }

  .holder {
    position: absolute; top: 344px; left: 0; right: 0; text-align: center;
  }
  .holder__name {
    font-weight: 700; font-size: 20px; color: var(--brand-red); letter-spacing: 0.3px; line-height: 24px;
  }
  .holder__role { font-size: 17px; color: var(--ink); line-height: 20px; }

  .icon-row {
    position: absolute; top: 396px; left: 87px; width: 190px; height: 24px;
  }
  .contact {
    position: absolute; top: 431px; left: 0; right: 0; text-align: center;
    font-size: 17px; line-height: 22px; color: var(--ink);
  }
  .divider {
    position: absolute; top: 507px; left: 88px; width: 194px; height: 1px; background: var(--rule);
  }
  .address {
    position: absolute; top: 517px; left: 0; right: 0; text-align: center;
    font-size: 17px; line-height: 22px; color: var(--ink);
  }
</style>
</head>
<body>
<div class="canvas">
  <section class="card card--front">
    <div class="wordmark">
      <span class="wordmark__main">ALPINE</span>
      <span class="wordmark__sub">COUNSEL</span>
    </div>

    <div class="holder">
      <div class="holder__name">DANIEL HARTLEY</div>
      <div class="holder__role">Managing Director</div>
    </div>

    <svg class="icon-row" viewBox="0 0 190 24" aria-hidden="true">
      <line x1="0" y1="12" x2="52" y2="12" stroke="#a8a8a8" stroke-width="1.2"/>
      <line x1="136" y1="12" x2="190" y2="12" stroke="#a8a8a8" stroke-width="1.2"/>
      <!-- phone -->
      <circle cx="67" cy="12" r="12" fill="#dc0201"/>
      <path d="M61 9 q6 -5 12 0 l-1.5 2 h-2 l-0.5 -1.5 h-4 l-0.5 1.5 h-2 z M62 17 l1.5 -5 h7 l1.5 5 z" fill="#fff"/>
      <!-- mail -->
      <circle cx="95" cy="12" r="12" fill="#dc0201"/>
      <rect x="88" y="7" width="14" height="10" fill="#fff"/>
      <polyline points="88,7 95,13 102,7" fill="none" stroke="#dc0201" stroke-width="1.2"/>
      <!-- globe -->
      <circle cx="123" cy="12" r="12" fill="#dc0201"/>
      <circle cx="123" cy="12" r="6.5" fill="none" stroke="#fff" stroke-width="1.5"/>
      <ellipse cx="123" cy="12" rx="2.8" ry="6.5" fill="none" stroke="#fff" stroke-width="1.2"/>
      <line x1="116.5" y1="12" x2="129.5" y2="12" stroke="#fff" stroke-width="1.2"/>
    </svg>

    <div class="contact">
      <div>044-987 654 321</div>
      <div>info@alpinecounsel.com</div>
      <div>www.alpinecounsel.com</div>
    </div>
    <div class="divider"></div>
    <div class="address">
      <div>18, Lindenweg Street,</div>
      <div>80312,Switzerland</div>
    </div>
  </section>

  <section class="card card--back">
    <div class="wordmark">
      <span class="wordmark__main">ALPINE</span>
      <span class="wordmark__sub">COUNSEL</span>
    </div>
  </section>
</div>
</body>
</html>
```